Rebranding Website – Tamsel Health Institute (40 Years)

Organization Description:
The Tamsel Health Institute (THI / www.tamselhi.nl) has been a trusted address for more than 40 years for people who choose a natural and sustainable approach to their health. We combine experience and history with a modern, professional approach.

Assignment:
Our current website is outdated and no longer reflects who we are today. We are looking for a new web design that aligns with our renewed logo and is both functional and inspiring. The website should have a clear structure, be user-friendly, and convey trust.

What we are looking for in the design:

A modern, fresh look that matches our logo and color palette logo in attachment.

Goal-oriented: simple and intuitive appointment scheduling.

Informative: space for a blog/news section to share knowledge and updates.

A dedicated page for each therapist with photo, expertise, and contact options.

A separate page for each type of therapy, with explanations and benefits.

A clear and visible link to our webshop (separate website).

Clear navigation and an organized menu structure.

Responsive design (desktop, tablet, mobile).

User-friendly CMS so we can manage and expand content ourselves.

Style Preferences:

- Color palette in line with our logo (green and natural tones, complemented by fresh and calm accents).
- Clean, professional design with plenty of white space.
- Accessible, warm, and inviting.

Functionalities:
- Online appointment scheduling or easy contact options.
- Blog/news section.
- Dedicated pages for therapists and therapies.
- Link to webshop.
- Possibility to expand the offer in the future (e.g., videos, downloads, or e-consultations).

What we would like to avoid:
- Pages that are too cluttered or confusing.
- Excessive text without clear structure.
- Stock photos lacking authenticity.

Target Audience:
People who consciously focus on their health, choose a natural approach, and are looking for a professional and reliable center where expertise and personal attention are central.

Additional Information:
The new website should bridge our 40-year history with the future. A place where visitors feel both familiar and inspired – and where they are immediately invited to get in touch, book an appointment, or visit our webshop.

You find our logo and impression in the uploads.

```html
<!DOCTYPE html>
<html lang="en">
<head>
<meta charset="utf-8">
<title>Tamsel Health Institute – Natural Healing</title>
<link href="https://fonts.googleapis.com/css2?family=Poppins:wght@400;500;600;700&family=Barlow:wght@400;500&display=swap" rel="stylesheet">
<style>
:root{
  --green:#7db442;
  --green-dark:#1f4d3b;
  --ink:#1b1b1b;
  --charcoal:#333333;
  --beige:#f5f1e0;
  --sky:#daebfb;
  --white:#ffffff;
  --muted:#6d6d6d;
  --gold:#c29a3a;
  --accent-yellow:#e2e85a;
}
*{margin:0;padding:0;box-sizing:border-box}
html,body{width:1200px;height:4135px;overflow:hidden}
body{font-family:"Poppins",sans-serif;color:var(--ink);position:relative;background:var(--white)}
.abs{position:absolute}
section,footer{position:absolute;left:0;width:1200px}

/* Hero */
.hero{top:0;height:741px;background:linear-gradient(180deg,#bfd8ea 0%,#dfeaf3 55%,#eef3f6 100%)}
.hero-photo{position:absolute;inset:0;background:radial-gradient(ellipse at 85% 75%,#f7f9fb 0 18%,transparent 40%),radial-gradient(ellipse at 30% 60%,rgba(90,130,60,.35) 0 10%,transparent 28%)}
.emergency{top:26px;right:210px;font-size:11px;color:#333}
.nav-pill{top:59px;left:194px;width:812px;height:58px;background:var(--white);border-radius:29px}
.logo-circle{top:40px;left:246px;width:112px;height:112px;border-radius:50%;background:var(--white);display:flex;align-items:center;justify-content:center;font-weight:700;font-size:28px;color:var(--charcoal)}
.nav{top:80px;left:474px;display:flex;gap:18px;font-size:12px;font-weight:500;color:#222}
.booking{top:72px;left:910px;width:84px;height:32px;border-radius:16px;background:var(--charcoal);color:#fff;font-size:11px;display:flex;align-items:center;justify-content:center}
.hero-title{top:246px;left:443px;font-size:48px;line-height:46px;font-weight:400;color:#1e1e1e}
.hero-title strong{font-weight:600;display:block}
.hero-text{top:356px;left:446px;width:460px;font-size:12px;font-weight:500;line-height:16px;color:#222}
.btn{background:var(--charcoal);color:#fff;font-size:12px;display:flex;align-items:center;justify-content:center;border-radius:3px}
.hero-btn{top:403px;left:447px;width:156px;height:40px}

/* Quote */
.quote{top:741px;height:257px;background:var(--green);color:#fff;text-align:center}
.quote h2{position:absolute;top:76px;left:0;width:1200px;font-size:24px;line-height:34px;font-weight:600}
.quote .by{position:absolute;top:156px;width:1200px;font-size:10px;font-weight:600}
.quote .role{position:absolute;top:170px;width:1200px;font-size:8px;opacity:.85}

/* Experience */
.experience{top:998px;height:526px;background:var(--beige)}
.section-title{font-weight:600;color:var(--green-dark);font-size:32px;line-height:42px}
.experience .section-title{top:112px;left:194px}
.badge{top:80px;left:852px;width:154px;height:154px;border-radius:50%;background:radial-gradient(circle,#d8b456 0 55%,var(--gold) 56% 100%)}
.feature{top:277px;width:254px;height:175px;background:#fff;border-radius:10px;padding:24px 26px}
.feature svg{display:block;margin-bottom:14px}
.feature h3{font-size:14px;font-weight:600;margin-bottom:20px}
.feature p{font-size:10px;line-height:17px;color:var(--muted)}

/* Telehealth */
.tele{top:1524px;height:431px;background:#2e7a52}
.tele-photo{position:absolute;inset:0;background:radial-gradient(ellipse at 12% 80%,#e6e0d0 0 8%,transparent 20%),radial-gradient(ellipse at 90% 60%,#d9e8dc 0 6%,transparent 16%),linear-gradient(135deg,#2f7d55,#277049)}
.tele-box{top:77px;left:363px;width:474px;height:279px;background:var(--charcoal);border-radius:6px;color:#fff}
.tele-box h2{position:absolute;top:50px;left:50px;font-size:25px;line-height:34px;font-weight:600}
.tele-box p{position:absolute;top:138px;left:46px;width:290px;font-size:11px;line-height:15px}
.tele-box p b{color:var(--accent-yellow);font-weight:600}
.tele-logo{top:143px;left:336px;width:88px;height:88px;border-radius:50%;background:#fff;color:var(--charcoal);font-weight:700;font-size:20px;display:flex;align-items:center;justify-content:center}

/* Services */
.services{top:1955px;height:749px;background:var(--sky)}
.services .section-title{top:110px;width:1200px;text-align:center}
.service{width:254px;height:117px;background:#fff;border-radius:10px}
.service .icon{position:absolute;top:26px;left:24px;width:40px;height:40px;border-radius:8px;background:#eef1f3}
.service h3{position:absolute;top:30px;left:92px;font-size:10px;font-weight:600}
.service p{position:absolute;top:52px;left:92px;width:150px;font-size:10px;line-height:17px;color:var(--muted)}

/* Results */
.results{top:2704px;height:542px;background:var(--green);color:#fff}
.results .section-title{top:112px;left:194px;color:#fff;font-size:32px;line-height:42px}
.stat{top:264px;width:190px}
.stat .num{font-size:24px;font-weight:600}
.stat .bar{margin-top:4px;height:5px;background:var(--charcoal);border-radius:3px;position:relative}
.stat .bar span{position:absolute;left:0;top:0;bottom:0;background:#fff;border-radius:3px}
.stat .lbl{margin-top:10px;font-size:9px;font-weight:600}
.results p{top:362px;left:194px;width:380px;font-size:10px;line-height:17px}
.results .btn{top:427px;left:194px;width:156px;height:40px}
.portrait{top:67px;left:597px;width:406px;height:406px;border-radius:50%;background:radial-gradient(circle at 35% 40%,#f2f2ea 0 14%,#5f8e3c 30%,#3d6b2b 100%)}

/* Integrative */
.integrative{top:3246px;height:474px;background:#fff}
.integrative .section-title{top:114px;left:194px}
.integrative .lead{top:112px;right:194px;width:190px;text-align:right;font-family:"Barlow",sans-serif;font-size:12px;line-height:19px;color:var(--green-dark)}
.action{top:278px;width:184px;height:119px;background:#fff;border-radius:10px;box-shadow:0 4px 18px rgba(0,0,0,.07)}
.action .go{position:absolute;top:16px;right:16px}
.action h3{position:absolute;top:67px;left:25px;font-size:12px;font-weight:500;line-height:17px}

/* Footer */
footer{top:3720px;height:415px;background:var(--charcoal);color:#fff}
.brand{top:80px;left:194px;font-size:25px;font-weight:700}
.tagline{top:135px;left:194px;font-size:12px;font-weight:600}
.f-lead{top:80px;left:749px;width:230px;font-size:11px;line-height:19px;color:#f3e4b5}
.phone{top:166px;left:749px;font-size:12px;font-weight:600;display:flex;align-items:center;gap:6px}
.col{top:222px;font-size:10px}
.col h4{font-size:12px;font-weight:600;margin-bottom:26px}
.col li{list-style:none;line-height:17px}
.f-logo{top:235px;left:745px;width:94px;height:94px;border-radius:50%;background:#fff;color:var(--charcoal);font-weight:700;font-size:20px;display:flex;align-items:center;justify-content:center}
.copy{top:365px;left:194px;font-size:9px}
.legal{top:365px;right:194px;font-size:9px;display:flex;gap:40px}
</style>
</head>
<body>

<section class="hero">
  <div class="hero-photo" role="img" aria-label="Photo of a glass vase with green herbs, small glass vials of homeopathic globules and a white mortar and pestle on a pale blue background"></div>
  <div class="abs emergency">For emergencies call &nbsp; + 11 555 010 20 30</div>
  <div class="abs nav-pill"></div>
  <div class="abs logo-circle">THI</div>
  <nav class="abs nav"><span>Home</span><span>About</span><span>Services</span><span>How it works</span><span>Program</span><span>Blog</span><span>Contact</span></nav>
  <div class="abs booking">Booking</div>
  <h1 class="abs hero-title">Discover the Power of<strong>Natural Healing</strong></h1>
  <p class="abs hero-text">Lorem ipsum dolor sit amet, consectetur adipiscing elit. Ut elit tellus, luctus nec ullamcorper mattis, pulvinar dapibus leo.</p>
  <div class="abs btn hero-btn">Discover More</div>
</section>

<section class="quote">
  <h2>The highest ideal of cure is rapid, gentle<br>and permanent restoration of health.</h2>
  <div class="by">Dr. Elias Varenholt</div>
  <div class="role">Founder of Homeopathy</div>
</section>

<section class="experience">
  <h2 class="abs section-title">Excellent heath to unlock the best<br>quality of your life</h2>
  <div class="abs badge" role="img" aria-label="Gold 40 years of experience seal"></div>
  <div class="abs feature" style="left:194px">
    <svg width="18" height="18" viewBox="0 0 24 24" fill="none" stroke="#1f4d3b" stroke-width="2"><circle cx="12" cy="12" r="3"/><circle cx="12" cy="12" r="8" stroke-dasharray="4 2"/></svg>
    <h3>Compassionate Team</h3>
    <p>Lorem ipsum dolor sit amet, consectetur adipiscing elit. Ut elit tellus, luctus nec ullamcorper mattis, pulvinar dapibus leo.</p>
  </div>
  <div class="abs feature" style="left:473px">
    <svg width="18" height="18" viewBox="0 0 24 24" fill="none" stroke="#1f4d3b" stroke-width="2"><path d="M12 20s-8-5-8-11a4 4 0 0 1 8-1 4 4 0 0 1 8 1c0 6-8 11-8 11z"/></svg>
    <h3>For Heal, Lasting Results</h3>
    <p>Lorem ipsum dolor sit amet, consectetur adipiscing elit. Ut elit tellus, luctus nec ullamcorper mattis, pulvinar dapibus leo.</p>
  </div>
  <div class="abs feature" style="left:752px">
    <svg width="18" height="18" viewBox="0 0 24 24" fill="none" stroke="#1f4d3b" stroke-width="2"><path d="M5 19C5 9 11 5 20 4c-1 9-5 15-15 15z"/><path d="M5 19l8-8"/></svg>
    <h3>Nature-First Solutions</h3>
    <p>Lorem ipsum dolor sit amet, consectetur adipiscing elit. Ut elit tellus, luctus nec ullamcorper mattis, pulvinar dapibus leo.</p>
  </div>
</section>

<section class="tele">
  <div class="tele-photo" role="img" aria-label="Flat lay of a mortar with flowers, vials of globules, capsules and a dropper bottle on a green surface"></div>
  <div class="abs tele-box">
    <h2>Are you unable to visit? Book<br>a telehealth consultation.</h2>
    <p>The Tamsel Health Institute (THI / www.tamselhi.nl) has been a trusted address for more than <b>40 years</b> for people who choose a natural and sustainable approach to their health. We combine experience and history with a modern, professional approach.</p>
    <div class="abs tele-logo">THI</div>
  </div>
</section>

<section class="services">
  <h2 class="abs section-title">Homeopathic treatments and<br>healing services</h2>
  <div class="abs service" style="left:194px;top:271px"><div class="icon" role="img" aria-label="Allergies icon"></div><h3>Allergies</h3><p>Lorem ipsum dolor sit amet, consectetur adipiscing elit.</p></div>
  <div class="abs service" style="left:473px;top:271px"><div class="icon" role="img" aria-label="Joint and muscle icon"></div><h3>Joint &amp; Muscle Pain</h3><p>Lorem ipsum dolor sit amet, consectetur adipiscing elit.</p></div>
  <div class="abs service" style="left:752px;top:271px"><div class="icon" role="img" aria-label="Fatigue icon"></div><h3>Chronic Fatigue</h3><p>Lorem ipsum dolor sit amet, consectetur adipiscing elit.</p></div>
  <div class="abs service" style="left:194px;top:414px"><div class="icon" role="img" aria-label="Lungs icon"></div><h3>Respiratory Problems</h3><p>Lorem ipsum dolor sit amet, consectetur adipiscing elit.</p></div>
  <div class="abs service" style="left:473px;top:414px"><div class="icon" role="img" aria-label="Mental health icon"></div><h3>Mental Health</h3><p>Lorem ipsum dolor sit amet, consectetur adipiscing elit.</p></div>
  <div class="abs service" style="left:752px;top:414px"><div class="icon" role="img" aria-label="Children's health icon"></div><h3>Children's Health</h3><p>Lorem ipsum dolor sit amet, consectetur adipiscing elit.</p></div>
  <div class="abs service" style="left:194px;top:557px"><div class="icon" role="img" aria-label="Women's health icon"></div><h3>Women's Health</h3><p>Lorem ipsum dolor sit amet, consectetur adipiscing elit.</p></div>
  <div class="abs service" style="left:473px;top:557px"><div class="icon" role="img" aria-label="Men's health icon"></div><h3>Men's Health</h3><p>Lorem ipsum dolor sit amet, consectetur adipiscing elit.</p></div>
  <div class="abs service" style="left:752px;top:557px"><div class="icon" role="img" aria-label="Geriatric health icon"></div><h3>Geriatric Health</h3><p>Lorem ipsum dolor sit amet, consectetur adipiscing elit.</p></div>
</section>

<section class="results">
  <h2 class="abs section-title">We will find the best<br>medicine for your<br>condition</h2>
  <div class="abs stat" style="left:194px"><div class="num">90%</div><div class="bar"><span style="width:90%"></span></div><div class="lbl">Overall health improvement</div></div>
  <div class="abs stat" style="left:409px"><div class="num">87%</div><div class="bar"><span style="width:87%"></span></div><div class="lbl">Symptom elimination</div></div>
  <p class="abs">Lorem ipsum dolor sit amet, consectetur adipiscing elit. Ut elit tellus, luctus nec ullamcorper mattis, pulvinar dapibus leo.</p>
  <div class="abs btn">Discover More</div>
  <div class="abs portrait" role="img" aria-label="Circular photo of a smiling therapist among green plants with a large white daisy"></div>
</section>

<section class="integrative">
  <h2 class="abs section-title">Start using integrative medicine to<br>help you heal and thrive</h2>
  <p class="abs lead">Lorem ipsum dolor sit amet, consectetur adipiscing elit. Ut elit tellus, luctus nec ullamcorper mattis, pulvinar dapibus leo.</p>
  <div class="abs action" style="left:194px"><svg class="go" width="26" height="26" viewBox="0 0 26 26"><circle cx="13" cy="13" r="13" fill="#5c5c5c"/><path d="M9 17l8-8M11 9h6v6" stroke="#fff" stroke-width="2" fill="none"/></svg><h3>Instant Telehealth<br>appointment</h3></div>
  <div class="abs action" style="left:403px"><svg class="go" width="26" height="26" viewBox="0 0 26 26"><circle cx="13" cy="13" r="13" fill="#1f4d3b"/><path d="M9 17l8-8M11 9h6v6" stroke="#fff" stroke-width="2" fill="none"/></svg><h3>Chat with a<br>homeopath online</h3></div>
  <div class="abs action" style="left:613px"><svg class="go" width="26" height="26" viewBox="0 0 26 26"><circle cx="13" cy="13" r="13" fill="#1f4d3b"/><path d="M9 17l8-8M11 9h6v6" stroke="#fff" stroke-width="2" fill="none"/></svg><h3>Buy homeopathic<br>medicine</h3></div>
  <div class="abs action" style="left:821px"><svg class="go" width="26" height="26" viewBox="0 0 26 26"><circle cx="13" cy="13" r="13" fill="#1f4d3b"/><path d="M9 17l8-8M11 9h6v6" stroke="#fff" stroke-width="2" fill="none"/></svg><h3>Your personal<br>homeopathic kit</h3></div>
</section>

<footer>
  <div class="abs brand">VERDA</div>
  <div class="abs tagline">Alternative medicine &amp; holistic health Pagecraft template kit</div>
  <p class="abs f-lead">Lorem ipsum dolor sit amet, consectetur adipiscing elit. Ut elit tellus, luctus nec ullamcorper mattis, pulvinar dapibus leo.</p>
  <div class="abs phone"><svg width="12" height="12" viewBox="0 0 24 24" fill="#fff"><path d="M6.6 10.8a15 15 0 0 0 6.6 6.6l2.2-2.2a1 1 0 0 1 1-.3 11 11 0 0 0 3.6.6 1 1 0 0 1 1 1V20a1 1 0 0 1-1 1A17 17 0 0 1 3 4a1 1 0 0 1 1-1h3.5a1 1 0 0 1 1 1 11 11 0 0 0 .6 3.6 1 1 0 0 1-.3 1z"/></svg>+ 11 555 010 20 30</div>
  <div class="abs col" style="left:194px"><h4>Browse</h4><ul><li>Home</li><li>About</li><li>Resources</li><li>Success stories</li></ul></div>
  <div class="abs col" style="left:354px"><h4>Resources</h4><ul><li>Membership</li><li>Podcast</li><li>Programs</li><li>Shop</li></ul></div>
  <div class="abs col" style="left:514px"><h4>Blog</h4><ul><li>Mindset</li><li>Tools</li><li>Training</li><li>Charity</li></ul></div>
  <div class="abs f-logo">THI</div>
  <div class="abs copy">Copyright © 2025 The Tamsel Health Institute , All rights reserved.</div>
  <div class="abs legal"><span>Cookies</span><span>Privacy Policy</span></div>
</footer>

</body>
</html>
```